Career Management Consultant Fun Professional Business Card

This is a business card for a personal career management consultant. The vibe needs to be professional but fun, modern with colour.

The name of the business is "Marcus Telwanger Career Management Consulting"

The name of the individual is "Marcus Telwanger" and his title is "Career Management Consultant"

Industry/Entity Type

Business

Contact Information for Business Card

Marcus Telwanger
Phone: 0400 827 316
Email: Marcus.Telwanger@mailvessa.com

```html
<!DOCTYPE html>
<html lang="en">
<head>
<meta charset="utf-8">
<title>Marcus Telwanger – Business Card</title>
<link rel="stylesheet" href="https://fonts.googleapis.com/css2?family=Noto+Sans:wght@400;700&display=swap">
<style>
  :root {
    --backdrop: #e9e4dc;
    --card-black: #000000;
    --accent-orange: #f5a01a;
    --accent-yellow: #ffe600;
    --text-orange: #f2a22a;
    --card-shadow: rgba(0, 0, 0, 0.28);
  }
  * { box-sizing: border-box; margin: 0; padding: 0; }
  html, body {
    width: 1200px;
    height: 900px;
    overflow: hidden;
    background: var(--backdrop);
    font-family: "Noto Sans", Verdana, sans-serif;
  }
  .sheet {
    width: 1200px;
    height: 900px;
    display: flex;
    flex-direction: column;
    align-items: center;
    justify-content: center;
    gap: 42px;
  }
  .card {
    position: relative;
    width: 700px;
    height: 400px;
    background: var(--card-black);
    box-shadow: 0 8px 22px var(--card-shadow);
    overflow: hidden;
    color: var(--text-orange);
  }
  .card__stripe {
    position: absolute;
    left: 0;
    right: 0;
    height: 15px;
    background: linear-gradient(90deg,
      var(--accent-orange) 0%,
      var(--accent-orange) 18%,
      var(--accent-yellow) 45%,
      var(--accent-orange) 75%,
      var(--accent-orange) 100%);
  }
  .card--front .card__stripe { top: 336px; }
  .card--back .card__stripe { top: 334px; }

  .front__identity {
    position: absolute;
    left: 262px;
    top: 148px;
  }
  .front__name {
    font-size: 40px;
    font-weight: 700;
    letter-spacing: 0.5px;
    line-height: 1.1;
  }
  .front__business {
    margin-top: 2px;
    margin-left: -12px;
    font-size: 21px;
    font-weight: 400;
  }

  .back__contact {
    position: absolute;
    left: 0;
    right: 0;
    top: 118px;
    display: flex;
    flex-direction: column;
    align-items: center;
    text-align: center;
  }
  .back__name {
    font-size: 22px;
    font-weight: 700;
    letter-spacing: 0.4px;
    margin-left: 50px;
  }
  .back__line {
    display: flex;
    align-items: center;
    gap: 8px;
    font-size: 22px;
    line-height: 1.35;
  }
  .back__line--phone { margin-left: -10px; }
  .back__icon {
    width: 20px;
    height: 20px;
    flex: none;
  }
</style>
</head>
<body>
  <main class="sheet">
    <section class="card card--front" aria-label="Business card front">
      <div class="front__identity">
        <h1 class="front__name">Marcus Telwanger</h1>
        <p class="front__business">Career Management Consulting</p>
      </div>
      <div class="card__stripe"></div>
    </section>

    <section class="card card--back" aria-label="Business card back">
      <div class="back__contact">
        <h2 class="back__name">Marcus Telwanger</h2>
        <p class="back__line back__line--phone">
          <svg class="back__icon" viewBox="0 0 20 20" aria-hidden="true">
            <circle cx="10" cy="10" r="8" fill="none" stroke="var(--text-orange)" stroke-width="1.6"/>
            <path d="M7 5.5c-1.2 1.8-.8 4.6 1.2 6.8s4.6 2.8 5.9 1.9l-1.6-2.1-1.6.7c-1-.6-2-1.8-2.4-3l1.4-1L8.9 6z" fill="var(--text-orange)"/>
          </svg>
          <span>0400 827 316</span>
        </p>
        <p class="back__line back__line--email">
          <svg class="back__icon" viewBox="0 0 20 20" aria-hidden="true">
            <rect x="2" y="4.5" width="16" height="11" fill="none" stroke="var(--text-orange)" stroke-width="1.4"/>
            <path d="M2 4.5l8 6.5 8-6.5M2 15.5l6-5.5M18 15.5l-6-5.5" fill="none" stroke="var(--text-orange)" stroke-width="1.4"/>
          </svg>
          <span>Marcus.Telwanger@mailvessa.com</span>
        </p>
      </div>
      <div class="card__stripe"></div>
    </section>
  </main>
</body>
</html>
```